Brindle Tavern & Lodge Supplies need a website

We need a website designed and created to facilitate us to promote & sell our products online. We buy excess / clearance lots of pub, cafe, restaurant & hotel furniture and equipment (usually from businesses that have excess inventory after a refurb or have closed down). We then sell these to other businesses mainly through our Chatterly page "Brindle Tavern & Lodge Supplies" but the process is cumbersome for the following reasons:
1) We dont have a stock list and images as it changes daily and people can only rely on recent posts and dont know if something is for sale still or is sold
2) we do not have the facility to sell online.

We are open to ideas and design concepts

We already have a logo & stationery deisgned

its probably best to look through our Chatterly page to better understand what we do

We would consider a catalogue / by department / category user interface such as:
https://brambleworth-trade-fittings.co.uk/

Our preference would be to change / delete / update stock via smartphone to best facilitate the maintenance of the website which i will do myself

Suggested categories would include:
Bar Furniture
Bar Equipment
Restaurant Furniture
Catering Equipment
Bedroom Furniture
Miscellaneous

Sub categories would include:
Bar Furniture:
Bar Stools
Bar Tables
Benches
Tub chairs
Arm chairs
Pub Mirrors
Pub Signs
Pub Memorabilia

Bar Equipment:
Bottle Coolers
Ice Machines
Glass Washers
Tills
Lighting
Sound
Wireless waiter
Glassware
Taps
Line coolers
Snooker tables
Pool tables
gaming machines

Restaurant Furniture:
Tables
Chairs
Wine racks
Dressers
Couches
Bench seating
Tub Chairs
Arm chairs
High chairs
Menu boards
Mirrors
Pictures

Catering Equipment:
Fridges
Freezers
Ovens
Cookers
Fryers
Carvery units
Hot display units
Refrigerated displays
Sinks
Stainless steel units
Microwaves
Mixers
Crockery
Cutlery
Utensils
Glassware

Bedroom Furniture:
Beds
Headboards
Wardrobes
Lockers
Dressing Tables
Mirrors
Lamps
Pictures

Profit sharing schemes:
Pool Tables
Juke Boxes
Gaming Machines

Target Market(s)

Pubs
Restaurants
cafes
guest houses
hotels

Industry/Entity Type

Hospitality

Number of Pages Required

5+ page

Colors

Designer to choose colors to be used in the design.

Requirements
Must have
• Website featuring our categories of stock to sell
Nice to have
• Ecommerce option
Should not have
• just a front page

```html
<!DOCTYPE html>
<html lang="en">
<head>
<meta charset="utf-8">
<title>Brindle Tavern &amp; Lodge Supplies</title>
<link href="https://fonts.googleapis.com/css2?family=Mulish:ital,wght@0,400;0,600;0,700;0,800;1,700&display=swap" rel="stylesheet">
<style>
:root{
  --red:#a50f1c;
  --red-dark:#8c0c17;
  --ink:#222;
  --text:#555;
  --muted:#888;
  --line:#dcdcdc;
  --black:#141414;
  --footer:#1f1f1f;
  --star:#b9c91d;
  --grey-icon:#6b6f73;
  --white:#fff;
}
*{box-sizing:border-box;margin:0;padding:0}
html,body{width:1200px;height:3863px;overflow:hidden}
body{position:relative;font-family:'Mulish',sans-serif;color:var(--ink);background:var(--white)}

/* header */
.site-header{position:absolute;left:0;top:0;width:1200px;height:90px;background:var(--red)}
.brand{position:absolute;left:0;top:0;width:400px;height:90px;background:var(--white);clip-path:polygon(0 0,100% 0,86% 100%,0 100%);display:flex;align-items:center;padding-left:112px;gap:10px}
.brand-mark{width:20px;height:20px;background:var(--red)}
.brand-name{font-weight:800;font-size:15px;color:var(--red);text-transform:uppercase;letter-spacing:.2px;width:200px;line-height:1.25}
.main-nav a{position:absolute;top:38px;color:var(--white);font-size:15px;text-decoration:none;font-weight:600}
.caret{display:inline-block;width:0;height:0;border-left:4px solid transparent;border-right:4px solid transparent;border-top:5px solid var(--white);margin-left:6px;vertical-align:middle}

/* hero */
.hero{position:absolute;left:0;top:90px;width:1200px;height:510px;background:linear-gradient(120deg,#3a3a2a 0%,#6b6a3a 30%,#2c2a22 55%,#5d5c34 80%,#2a281f 100%)}
.hero::after{content:"";position:absolute;inset:0;background:rgba(0,0,0,.35);z-index:1}
.hero-title{position:absolute;top:156px;left:0;width:1200px;text-align:center;color:var(--white);font-weight:700;font-size:44px;line-height:1.2;z-index:2;text-shadow:0 2px 6px rgba(0,0,0,.35)}
.search-bar{position:absolute;left:165px;top:335px;width:870px;height:98px;background:rgba(20,20,20,.88);z-index:2}
.field{position:absolute;top:363px;height:44px;background:var(--white);font-size:14px;color:var(--muted);padding:13px 18px;z-index:3}
.field .sep{position:absolute;right:34px;top:6px;bottom:6px;border-left:1px solid var(--line)}
.field .tri{position:absolute;right:13px;top:19px;border-left:5px solid transparent;border-right:5px solid transparent;border-top:6px solid #555}
.search-btn{position:absolute;left:894px;top:363px;width:118px;height:44px;background:var(--red);color:var(--white);font-weight:800;font-size:14px;text-align:center;line-height:44px;letter-spacing:.5px;z-index:3}
.dropdown{position:absolute;left:417px;top:407px;width:247px;height:417px;background:var(--white);box-shadow:0 4px 12px rgba(0,0,0,.25);z-index:4;list-style:none;padding:30px 0 0 33px}
.dropdown li{font-size:13px;color:#555;height:26.5px}

/* results */
.results-bar{position:absolute;left:100px;top:708px;width:1000px;height:47px;background:var(--black);color:var(--white);font-size:14px}
.results-bar span{position:absolute;top:15px}
.compact{text-decoration:underline}

.card{position:absolute;left:100px;width:1000px;height:232px;border:1px solid var(--line);border-radius:3px;background:var(--white)}
.card .photo{position:absolute;left:26px;top:18px;width:219px;height:165px}
.card h2{position:absolute;left:284px;top:36px;font-size:24px;font-weight:600;color:var(--ink)}
.price{position:absolute;top:32px;font-style:italic;font-weight:700;color:var(--red);font-size:28px}
.price small{font-size:12px;font-weight:400;color:var(--muted);margin-left:6px}
.actions{position:absolute;top:36px;display:flex;gap:8px}
.icon{width:34px;height:34px;border-radius:4px;display:flex;align-items:center;justify-content:center}
.icon.info{background:var(--red)}
.icon.mail{background:var(--grey-icon)}
.stars{position:absolute;left:284px;top:87px;display:flex;gap:2px}
.desc{position:absolute;left:284px;top:126px;width:700px;font-size:13px;line-height:28.5px;color:var(--text)}
.desc a{color:var(--red);text-decoration:none}

.pagination{position:absolute;left:100px;top:3446px;display:flex;gap:8px}
.pagination span{height:24px;min-width:24px;padding:0 8px;border:1px solid var(--line);font-size:11px;line-height:22px;text-align:center;color:#555;border-radius:2px}
.pagination .dark{background:#444;color:var(--white);border-color:#444;width:50px}
.pagination .active{background:var(--red);color:var(--white);border-color:var(--red)}

/* footer */
.site-footer{position:absolute;left:0;top:3605px;width:1200px;height:258px;background:var(--footer);border-top:4px solid var(--red);color:var(--white)}
.social{position:absolute;left:467px;top:60px;display:flex;gap:6px}
.social span{width:40px;height:40px;border:2px solid var(--white);border-radius:50%}
.footer-nav{position:absolute;top:133px;left:0;width:1200px;text-align:center;font-size:15px;word-spacing:4px}
.footer-nav i{font-style:normal;margin:0 22px}
.copyright{position:absolute;top:178px;left:0;width:1200px;text-align:center;font-size:12px;color:#ccc}
</style>
</head>
<body>

<header class="site-header">
  <div class="brand"><span class="brand-mark"></span><span class="brand-name">Brindle Tavern &amp; Lodge Supplies</span></div>
  <nav class="main-nav">
    <a style="left:522px">Home</a>
    <a style="left:600px">Categories<span class="caret"></span></a>
    <a style="left:726px">Shops<span class="caret"></span></a>
    <a style="left:823px">Information</a>
    <a style="left:937px">Log in</a>
    <a style="left:1018px">Register</a>
  </nav>
</header>

<section class="hero" role="img" aria-label="Rows of upholstered olive bar chairs">
  <h1 class="hero-title">Brindle Tavern &amp; Lodge Supplies</h1>
</section>

<div class="search-bar"></div>
<div class="field" style="left:185px;width:222px">Keywords..</div>
<div class="field" style="left:417px;width:247px;color:#444">Bar Equipment<span class="sep"></span><span class="tri"></span></div>
<div class="field" style="left:672px;width:214px;color:#444">Newest<span class="sep"></span><span class="tri"></span></div>
<div class="search-btn">SEARCH</div>
<ul class="dropdown">
  <li>Bottle Coolers</li><li>Ice Machines</li><li>Glass Washers</li><li>Tills</li><li>Lighting</li><li>Sound</li><li>Wireless waiter</li><li>Glassware</li><li>Taps</li><li>Line coolers</li><li>Snooker tables</li><li>Pool tables</li><li>gaming machines</li>
</ul>

<div class="results-bar">
  <span style="left:28px">1 to 10 of 1301</span>
  <span class="compact" style="left:714px">Compact view</span>
  <span style="left:863px">Expanded view</span>
</div>

<svg width="0" height="0" style="position:absolute">
  <defs>
    <symbol id="star" viewBox="0 0 20 20"><path d="M10 1l2.6 6 6.4.5-4.9 4.2 1.5 6.3L10 14.7 4.4 18l1.5-6.3L1 7.5 7.4 7z" fill="#b9c91d"/></symbol>
    <symbol id="i-info" viewBox="0 0 20 20"><circle cx="10" cy="10" r="8" fill="none" stroke="#fff" stroke-width="2"/><rect x="9" y="8.5" width="2" height="6" fill="#fff"/><circle cx="10" cy="6" r="1.2" fill="#fff"/></symbol>
    <symbol id="i-mail" viewBox="0 0 20 20"><rect x="2" y="4" width="16" height="12" rx="1" fill="#fff"/><path d="M2.5 5l7.5 6 7.5-6" fill="none" stroke="#6b6f73" stroke-width="1.5"/></symbol>
    <symbol id="stars5" viewBox="0 0 100 18"><use href="#star" x="0" width="18" height="18"/><use href="#star" x="20" width="18" height="18"/><use href="#star" x="40" width="18" height="18"/><use href="#star" x="60" width="18" height="18"/><use href="#star" x="80" width="18" height="18"/></symbol>
  </defs>
</svg>

<article class="card" style="top:811px">
  <div class="photo" role="img" aria-label="Red leather bar chairs" style="background:linear-gradient(135deg,#5a3a2c,#a8474a 60%,#3b2a24)"></div>
  <h2>Bar Furniture</h2>
  <div class="price" style="left:490px">£10<small>VAT Free</small></div>
  <div class="actions" style="left:647px"><span class="icon info"><svg width="20" height="20"><use href="#i-info"/></svg></span><span class="icon mail"><svg width="20" height="20"><use href="#i-mail"/></svg></span></div>
  <svg class="stars" width="100" height="18"><use href="#stars5"/></svg>
  <p class="desc">At vero eos et accusamus et iusto odio dignissimos ducimus qui blanditiis praesentium voluptatum deleniti atque corrupti quos dolores et quas molestias excepturi sint occaecati cupiditate non provident, similique sunt in culpa qui officia deserunt mollitia animi, id est laborum. &nbsp;......<a>more</a></p>
</article>

<article class="card" style="top:1074px">
  <div class="photo" role="img" aria-label="Glass-door bottle coolers" style="background:linear-gradient(135deg,#5d605e,#b9bdb8 50%,#4a4c4a)"></div>
  <h2>Bar Equipment</h2>
  <div class="price" style="left:490px">£10<small>VAT Free</small></div>
  <div class="actions" style="left:647px"><span class="icon info"><svg width="20" height="20"><use href="#i-info"/></svg></span><span class="icon mail"><svg width="20" height="20"><use href="#i-mail"/></svg></span></div>
  <svg class="stars" width="100" height="18"><use href="#stars5"/></svg>
  <p class="desc">At vero eos et accusamus et iusto odio dignissimos ducimus qui blanditiis praesentium voluptatum deleniti atque corrupti quos dolores et quas molestias excepturi sint occaecati cupiditate non provident, similique sunt in culpa qui officia deserunt mollitia animi, id est laborum. &nbsp;......<a>more</a></p>
</article>

<article class="card" style="top:1337px">
  <div class="photo" role="img" aria-label="Wooden restaurant tables and chairs" style="background:linear-gradient(135deg,#3a2c22,#7a5a3e 55%,#2e241d)"></div>
  <h2>Restaurant Furniture</h2>
  <div class="price" style="left:585px">£10<small>VAT Free</small></div>
  <div class="actions" style="left:739px"><span class="icon info"><svg width="20" height="20"><use href="#i-info"/></svg></span><span class="icon mail"><svg width="20" height="20"><use href="#i-mail"/></svg></span></div>
  <svg class="stars" width="100" height="18"><use href="#stars5"/></svg>
  <p class="desc">At vero eos et accusamus et iusto odio dignissimos ducimus qui blanditiis praesentium voluptatum deleniti atque corrupti quos dolores et quas molestias excepturi sint occaecati cupiditate non provident, similique sunt in culpa qui officia deserunt mollitia animi, id est laborum. &nbsp;......<a>more</a></p>
</article>

<article class="card" style="top:1600px">
  <div class="photo" role="img" aria-label="Stainless steel catering counter" style="background:linear-gradient(135deg,#2c2c2c,#8c8c88 55%,#3a3a38)"></div>
  <h2>Catering Equipment</h2>
  <div class="price" style="left:585px">£10<small>VAT Free</small></div>
  <div class="actions" style="left:739px"><span class="icon info"><svg width="20" height="20"><use href="#i-info"/></svg></span><span class="icon mail"><svg width="20" height="20"><use href="#i-mail"/></svg></span></div>
  <svg class="stars" width="100" height="18"><use href="#stars5"/></svg>
  <p class="desc">At vero eos et accusamus et iusto odio dignissimos ducimus qui blanditiis praesentium voluptatum deleniti atque corrupti quos dolores et quas molestias excepturi sint occaecati cupiditate non provident, similique sunt in culpa qui officia deserunt mollitia animi, id est laborum. &nbsp;......<a>more</a></p>
</article>

<article class="card" style="top:1863px">
  <div class="photo" role="img" aria-label="Red upholstered sofa" style="background:linear-gradient(135deg,#4a1a20,#a3303a 55%,#5a2026)"></div>
  <h2>Bedroom Furniture</h2>
  <div class="price" style="left:585px">£10<small>VAT Free</small></div>
  <div class="actions" style="left:739px"><span class="icon info"><svg width="20" height="20"><use href="#i-info"/></svg></span><span class="icon mail"><svg width="20" height="20"><use href="#i-mail"/></svg></span></div>
  <svg class="stars" width="100" height="18"><use href="#stars5"/></svg>
  <p class="desc">At vero eos et accusamus et iusto odio dignissimos ducimus qui blanditiis praesentium voluptatum deleniti atque corrupti quos dolores et quas molestias excepturi sint occaecati cupiditate non provident, similique sunt in culpa qui officia deserunt mollitia animi, id est laborum. &nbsp;......<a>more</a></p>
</article>

<article class="card" style="top:2126px">
  <div class="photo" role="img" aria-label="Cream leather armchair" style="background:linear-gradient(135deg,#2a2622,#d8d2c0 50%,#3a342c)"></div>
  <h2>Miscellaneous</h2>
  <div class="price" style="left:490px">£10<small>VAT Free</small></div>
  <div class="actions" style="left:647px"><span class="icon info"><svg width="20" height="20"><use href="#i-info"/></svg></span><span class="icon mail"><svg width="20" height="20"><use href="#i-mail"/></svg></span></div>
  <svg class="stars" width="100" height="18"><use href="#stars5"/></svg>
  <p class="desc">At vero eos et accusamus et iusto odio dignissimos ducimus qui blanditiis praesentium voluptatum deleniti atque corrupti quos dolores et quas molestias excepturi sint occaecati cupiditate non provident, similique sunt in culpa qui officia deserunt mollitia animi, id est laborum. &nbsp;......<a>more</a></p>
</article>

<article class="card" style="top:2389px">
  <div class="photo" role="img" aria-label="Stack of round padded bar stools" style="background:linear-gradient(135deg,#1e1a16,#cfc3a8 50%,#2a221c)"></div>
  <h2>Bar Stools</h2>
  <div class="price" style="left:490px">£10<small>VAT Free</small></div>
  <div class="actions" style="left:647px"><span class="icon info"><svg width="20" height="20"><use href="#i-info"/></svg></span><span class="icon mail"><svg width="20" height="20"><use href="#i-mail"/></svg></span></div>
  <svg class="stars" width="100" height="18"><use href="#stars5"/></svg>
  <p class="desc">At vero eos et accusamus et iusto odio dignissimos ducimus qui blanditiis praesentium voluptatum deleniti atque corrupti quos dolores et quas molestias excepturi sint occaecati cupiditate non provident, similique sunt in culpa qui officia deserunt mollitia animi, id est laborum. &nbsp;......<a>more</a></p>
</article>

<article class="card" style="top:2652px">
  <div class="photo" role="img" aria-label="Pub interior with wall mirrors" style="background:linear-gradient(135deg,#7a2a30,#b89a7a 55%,#3e2e26)"></div>
  <h2>Pub Mirrors</h2>
  <div class="price" style="left:490px">£10<small>VAT Free</small></div>
  <div class="actions" style="left:647px"><span class="icon info"><svg width="20" height="20"><use href="#i-info"/></svg></span><span class="icon mail"><svg width="20" height="20"><use href="#i-mail"/></svg></span></div>
  <svg class="stars" width="100" height="18"><use href="#stars5"/></svg>
  <p class="desc">At vero eos et accusamus et iusto odio dignissimos ducimus qui blanditiis praesentium voluptatum deleniti atque corrupti quos dolores et quas molestias excepturi sint occaecati cupiditate non provident, similique sunt in culpa qui officia deserunt mollitia animi, id est laborum. &nbsp;......<a>more</a></p>
</article>

<article class="card" style="top:2915px">
  <div class="photo" role="img" aria-label="Illuminated arcade machines and signs" style="background:linear-gradient(135deg,#0e0e14,#5a2a3a 50%,#14141c)"></div>
  <h2>Pub Signs</h2>
  <div class="price" style="left:490px">£10<small>VAT Free</small></div>
  <div class="actions" style="left:647px"><span class="icon info"><svg width="20" height="20"><use href="#i-info"/></svg></span><span class="icon mail"><svg width="20" height="20"><use href="#i-mail"/></svg></span></div>
  <svg class="stars" width="100" height="18"><use href="#stars5"/></svg>
  <p class="desc">At vero eos et accusamus et iusto odio dignissimos ducimus qui blanditiis praesentium voluptatum deleniti atque corrupti quos dolores et quas molestias excepturi sint occaecati cupiditate non provident, similique sunt in culpa qui officia deserunt mollitia animi, id est laborum. &nbsp;......<a>more</a></p>
</article>

<article class="card" style="top:3178px">
  <div class="photo" role="img" aria-label="Assorted light fittings" style="background:linear-gradient(135deg,#c8c4c4,#8a3036 50%,#e2dede)"></div>
  <h2>Lighting</h2>
  <div class="price" style="left:490px">£10<small>VAT Free</small></div>
  <div class="actions" style="left:647px"><span class="icon info"><svg width="20" height="20"><use href="#i-info"/></svg></span><span class="icon mail"><svg width="20" height="20"><use href="#i-mail"/></svg></span></div>
  <svg class="stars" width="100" height="18"><use href="#stars5"/></svg>
  <p class="desc">At vero eos et accusamus et iusto odio dignissimos ducimus qui blanditiis praesentium voluptatum deleniti atque corrupti quos dolores et quas molestias excepturi sint occaecati cupiditate non provident, similique sunt in culpa qui officia deserunt mollitia animi, id est laborum. &nbsp;......<a>more</a></p>
</article>

<nav class="pagination">
  <span class="dark">Prev</span><span class="active">1</span><span>2</span><span>3</span><span>4</span><span>5</span><span>6</span><span>...</span><span>22</span><span style="width:50px">Next</span>
</nav>

<footer class="site-footer">
  <div class="social" aria-label="Social links">
    <span title="Chatterly"></span><span></span><span></span><span></span><span></span><span></span>
  </div>
  <div class="footer-nav">Home<i>/</i>Categories<i>/</i>Shops<i>/</i>Information<i>/</i>Log in<i>/</i>Register</div>
  <div class="copyright">© Copyright 2018 Brindle Tavern &amp; Lodge Supplies. All Rights Reserved</div>
</footer>

</body>
</html>
```